Business Card Design

I need a business card for my baking business. Name of the company is Whisked by Tessa. I specialize in cookies and pies.
I don't make cupcakes or cakes. I would like a design with colors of brown, light pink and dark pink and maybe have the half eaten cookie be the dot of the "I" in my name. (Half eaten chocolate chip and the chips being hot pink light pink and brown chips).. I would like the card fun and modern design.
On the back of the card tag line- let me bake your day

Industry/Entity Type

Business

Contact Information for Business Card

Tessa Mernholt
Cell 5093617284
Email-Tesmern47@quillpost.net

```html
<!DOCTYPE html>
<html lang="en">
<head>
<meta charset="UTF-8">
<title>Whisked by Tessa — Business Card</title>
<link rel="stylesheet" href="https://fonts.googleapis.com/css2?family=Open+Sans:wght@400;600;700&family=Oswald:wght@400;500&display=swap">
<style>
  :root {
    --canvas: #000000;
    --card: #fde9ec;
    --stripe-faint: #f8dde2;
    --stripe-band: #f6c9d0;
    --pink-dark: #e9609b;
    --pink-logo: #ec6fa6;
    --brown: #7a4f2e;
    --ink: #1f1a1a;
    --cookie-light: #dcbd85;
    --cookie: #c9a66b;
    --cookie-deep: #a9854c;
  }
  * { box-sizing: border-box; margin: 0; padding: 0; }
  html, body {
    width: 1200px; height: 1200px; overflow: hidden;
    background: var(--canvas);
    font-family: "Open Sans", Arial, sans-serif;
  }
  .sheet {
    position: relative; width: 1200px; height: 1200px;
    display: flex; align-items: center; justify-content: center; gap: 40px;
  }
  .card {
    position: relative; width: 540px; height: 309px;
    background-color: var(--card);
    overflow: hidden;
  }
  .card--front {
    background-image: repeating-linear-gradient(
      to bottom, transparent 0 6px, var(--stripe-faint) 6px 7px);
  }
  .brand-name {
    font-family: "Open Sans", Arial, sans-serif;
    font-weight: 700;
    color: var(--pink-logo);
    white-space: nowrap;
    display: flex; align-items: center; gap: 10px;
  }
  .brand-dot {
    display: inline-block; border-radius: 50%;
    background: radial-gradient(circle at 40% 35%, var(--cookie-light), var(--cookie) 60%, var(--cookie-deep));
  }
  .card--front .brand-name {
    position: absolute; left: 38px; top: 62px; font-size: 25px;
  }
  .card--front .brand-dot { width: 30px; height: 30px; }
  .holder {
    position: absolute; right: 30px; top: 30px; text-align: left;
  }
  .holder__name {
    color: var(--pink-dark); font-weight: 600; font-size: 16px; line-height: 1.3;
  }
  .holder__role {
    color: var(--ink); font-size: 13.5px; line-height: 1.3;
  }
  .contact {
    position: absolute; left: 25px; bottom: 22px;
    color: var(--brown); font-size: 13px; line-height: 21px;
    border-collapse: collapse;
  }
  .contact th { font-weight: 400; text-align: left; width: 45px; }
  .contact .sep { width: 12px; }
  .cookie-bite {
    position: absolute; left: 408px; top: 164px;
    width: 210px; height: 210px; border-radius: 50%;
    background: radial-gradient(circle at 38% 35%, var(--cookie-light) 0%, var(--cookie) 55%, var(--cookie-deep) 100%);
  }
  .card--back .band {
    position: absolute; left: 0; right: 0; top: 108px; height: 84px;
    background-image: repeating-linear-gradient(
      to bottom, var(--stripe-band) 0 3px, transparent 3px 9px);
  }
  .card--back .brand-name {
    position: absolute; left: 50%; top: 128px; transform: translateX(-50%);
    font-size: 32px;
  }
  .card--back .brand-dot { width: 36px; height: 36px; }
  .tagline {
    position: absolute; left: 0; right: 0; top: 236px; text-align: center;
    font-family: "Oswald", "Arial Narrow", sans-serif;
    font-weight: 500;
    color: var(--brown); font-size: 18px;
  }
</style>
</head>
<body>
  <main class="sheet">
    <section class="card card--front">
      <div class="brand-name">Whisked by Tessa <span class="brand-dot"></span></div>
      <div class="holder">
        <p class="holder__name">Tessa Mernholt</p>
        <p class="holder__role">Managing Director</p>
      </div>
      <table class="contact">
        <tr><th>Tel</th><td class="sep">:</td><td>5093617284</td></tr>
        <tr><th>E-mail</th><td class="sep">:</td><td>Tesmern47@quillpost.net</td></tr>
        <tr><th>Web</th><td class="sep">:</td><td>www.whiskedbytessa.com</td></tr>
      </table>
      <div class="cookie-bite" role="img" aria-label="Illustration of a large bitten chocolate chip cookie peeking in from the corner"></div>
    </section>

    <section class="card card--back">
      <div class="band"></div>
      <div class="brand-name">Whisked by Tessa <span class="brand-dot"></span></div>
      <p class="tagline">let me bake your day</p>
    </section>
  </main>
</body>
</html>
```